HMC Business Card Design

We need a business card design for a new company called ' Harbour Mill Coffee'. We are a mobile Coffee Trailer providing Espresso Coffee, Specialty Tea's, Milkshakes, Iced Coffee & Iced Chocolate, Soft drinks and Gourmet Cookies to Sporting Events, Fetes, Animal Shows etc...
We would like Darren's name and mobile phone number on the card along with the harbour mill email address and a link to our facebook page Harbour Mill Coffee.
Can you please attach the Harbour Mill Logo to the business card.
I have tried to attach our logo and a picture of our mobile trailer to give you an idea of how we would like the design similar to the trailer if possible. If these pictures and logo's are not attached please email me and i will send them through.

Contact Information for Business Card

Darren Wilkes
0491 372 806
harbourmillcoffee@mailbox-demo.net
FB Harbour Mill Coffee

Requirements
Must have
• We would like coffee beans in the back ground of the card.

```html
<!DOCTYPE html>
<html lang="en">
<head>
<meta charset="utf-8">
<title>Harbour Mill Coffee – Business Card</title>
<link rel="stylesheet" href="https://fonts.googleapis.com/css2?family=Courier+Prime&display=swap">
<style>
  :root {
    --page-bg: #f2f2f2;
    --card-bg: #f7f7f5;
    --ink: #2a2624;
    --bean: #7a4a2e;
    --bean-light: #9a6444;
    --brand: #6e1a1f;
    --social: #3b5998;
  }
  * { box-sizing: border-box; margin: 0; padding: 0; }
  html, body {
    width: 1200px; height: 873px; overflow: hidden;
    background: var(--page-bg);
    font-family: "Courier Prime", "Courier New", monospace;
    color: var(--ink);
  }
  .sheet {
    width: 1200px; height: 873px;
    display: flex; align-items: center; justify-content: center; gap: 60px;
  }
  .card {
    position: relative;
    width: 500px; height: 286px;
    background: var(--card-bg);
    box-shadow: 0 2px 10px rgba(0,0,0,.15);
  }
  /* contact side */
  .bean {
    position: absolute; display: block;
    background: var(--bean); border-radius: 50%;
  }
  .bean--large { width: 54px; height: 32px; }
  .bean--small { width: 18px; height: 12px; background: var(--bean-light); position: static; display: inline-block; margin-right: 4px; vertical-align: middle; }
  .bean--title-start { left: 26px; top: 22px; transform: rotate(-8deg); }
  .bean--title-end { right: 24px; top: 198px; transform: rotate(10deg); }
  .card__title {
    position: absolute; left: 94px; top: 18px;
    font-size: 30px; font-weight: 400; letter-spacing: .5px;
  }
  .card__tagline {
    position: absolute; left: 150px; top: 56px;
    font-size: 20px;
  }
  .contact {
    position: absolute; top: 104px;
    font-size: 21px; line-height: 1.45;
  }
  .contact--primary { left: 32px; }
  .contact--secondary { left: 232px; top: 168px; }
  .contact__phone { letter-spacing: 1px; padding-left: 22px; }
  .links {
    position: absolute; left: 14px; bottom: 14px;
    font-size: 18px; line-height: 1.3;
  }
  .links__row { display: flex; align-items: center; gap: 4px; }
  .links__square { width: 14px; height: 14px; background: var(--social); }
  .links__mail { width: 16px; height: 14px; }
  /* logo side */
  .card--back { display: flex; align-items: center; justify-content: center; gap: 14px; }
  .brand-dot { width: 22px; height: 22px; border-radius: 50%; background: var(--brand); }
  .brand-name { font-size: 30px; color: var(--brand); }
</style>
</head>
<body>
<main class="sheet">
  <section class="card card--front" aria-label="Card front with contact details">
    <span class="bean bean--large bean--title-start" role="img" aria-label="Coffee bean"></span>
    <h1 class="card__title">Harbour Mill Coffee</h1>
    <p class="card__tagline">mobile Coffee Trailer</p>
    <span class="bean bean--large bean--title-end" role="img" aria-label="Coffee bean"></span>

    <div class="contact contact--primary">
      <p><span class="bean bean--small" role="img" aria-label="Coffee bean"></span>Darren Wilkes</p>
      <p class="contact__phone">0491 372 806</p>
    </div>
    <div class="contact contact--secondary">
      <p><span class="bean bean--small" role="img" aria-label="Coffee bean"></span>Leah Morton</p>
      <p class="contact__phone">0487 215 349</p>
    </div>

    <div class="links">
      <p class="links__row"><span class="links__square"></span>Harbour Mill Coffee</p>
      <p class="links__row">
        <svg class="links__mail" viewBox="0 0 16 14" aria-hidden="true">
          <rect x="1" y="1" width="14" height="12" fill="none" stroke="#2a2624" stroke-width="1.4"/>
          <polyline points="1,1 8,8 15,1" fill="none" stroke="#2a2624" stroke-width="1.4"/>
        </svg>harbourmillcoffee@mailbox-demo.net
      </p>
    </div>
  </section>

  <section class="card card--back" aria-label="Card back with brand name">
    <span class="brand-dot"></span>
    <p class="brand-name">Harbour Mill Coffee</p>
  </section>
</main>
</body>
</html>
```